Business Card Design

- one on one personal training
- group personal training
- indoor or outdoor training available
- fitness and health assessments
- personalised fitness programs
- flexible hours for training

I am a Personal Trainer in Perth Australia. I am looking to expand my word of mouth client base.

I would like to see something that uses the colours blue, green and/or yellow.

The final design should reflect the way that I train clients, fun, motivating and perhaps a little quirky?
Updates

update with a logo with the letters MPT thank you

Hi all, Have had some great designs so far. Have decided to go double sided, perhaps to use the back to list my services. Thank you

Please check update brief. Thank you.

Target Market(s)

Professionals, ages 30 to 60

Industry/Entity Type

Training

Contact Information for Business Card

Mira Ostrowski
Personal Trainer

0491 570 118
mirapersonaltrainer@quillnest.com
http://www.mirapersonaltrainer.net

Requirements
Must have
• A logo with the letter MPT
Nice to have
• a logo to represent either; fitness, health, change, overall well-being.
Should not have
• Please no weights or lotus flowers!!

```html
<!DOCTYPE html>
<html lang="en">
<head>
<meta charset="utf-8">
<title>Mira Ostrowski – Personal Trainer Business Card</title>
<link rel="stylesheet" href="https://fonts.googleapis.com/css2?family=Iceland&family=Open+Sans:wght@400&display=swap">
<style>
  :root {
    --card-bg: #000000;
    --accent-blue: #5cc8f2;
  }
  html, body {
    margin: 0;
    padding: 0;
    width: 1200px;
    height: 741px;
    overflow: hidden;
    background: var(--card-bg);
  }
  .business-card {
    position: relative;
    width: 1200px;
    height: 741px;
    background: var(--card-bg);
    color: var(--accent-blue);
    overflow: hidden;
  }
  .line {
    position: absolute;
    left: 0;
    width: 100%;
    margin: 0;
    font-weight: 400;
    text-align: center;
    white-space: nowrap;
    transform: translateY(-50%);
    line-height: 1;
  }
  .brand-name {
    top: 118px;
    font-family: "Open Sans", sans-serif;
    font-size: 96px;
    letter-spacing: 4px;
  }
  .bar-line {
    position: absolute;
    top: 0;
    left: 0;
  }
  .trainer-name {
    top: 245px;
    font-family: "Iceland", sans-serif;
    font-size: 68px;
    font-variant: small-caps;
    letter-spacing: 3px;
  }
  .trainer-role {
    top: 318px;
    font-family: "Iceland", sans-serif;
    font-size: 34px;
    text-transform: uppercase;
    letter-spacing: 2px;
  }
  .contact-phone {
    top: 384px;
    font-family: "Iceland", sans-serif;
    font-size: 40px;
    letter-spacing: 2px;
  }
  .contact-email,
  .contact-web {
    font-family: "Iceland", sans-serif;
    font-size: 30px;
    text-transform: uppercase;
    letter-spacing: 1px;
  }
  .contact-email { top: 434px; }
  .contact-web { top: 482px; }
  .service-list {
    font-family: "Open Sans", sans-serif;
    font-size: 31px;
  }
  .service-list .sep {
    padding: 0 10px;
  }
  .services-row-1 { top: 558px; }
  .services-row-2 { top: 608px; }
  .services-row-3 { top: 659px; }
</style>
</head>
<body>
  <main class="business-card">
    <svg class="bar-line" width="1200" height="741" aria-hidden="true">
      <rect x="92" y="184" width="1016" height="6" fill="var(--accent-blue)"/>
    </svg>

    <div class="line brand-name">MPT</div>

    <h1 class="line trainer-name">Mira Ostrowski</h1>
    <p class="line trainer-role">Personal Trainer</p>

    <p class="line contact-phone">0491 570 118</p>
    <p class="line contact-email">mirapersonaltrainer@quillnest.com</p>
    <p class="line contact-web">www.mirapersonaltrainer.net</p>

    <p class="line service-list services-row-1">
      <span class="sep">|</span>one on one personal training<span class="sep">|</span> indoor or outdoor training available<span class="sep">|</span>
    </p>
    <p class="line service-list services-row-2">
      <span class="sep">|</span>group personal training<span class="sep">|</span> fitness and health assessments<span class="sep">|</span>
    </p>
    <p class="line service-list services-row-3">
      <span class="sep">|</span>personalised fitness programs<span class="sep">|</span>
    </p>
  </main>
</body>
</html>
```